The Verdant Fiber Collective Review (VFCR) cover page.

We need a unique green font that will be superimposed on all issues of an electronic magazine. It will always have an image in the background referring to one of the articles in each particular number.
The cover of the magazine should read the motto of the Verdant Fiber Collective: "The RVFC lifts Fiber Craft and inspires a Bright Tomorrow."

​

On the back cover, the editor in chief, the editorial committee, the legal notice and the three logos (TLOK, Ravendix, and the society logo) should be mentioned. see power point page.
​

On the back cover, the editor in chief, the editorial committee, the legal notice and the three logos (TLOK, Ravendix, ans the society logo) should be mentioned.

Target Market(s)

The journal will be initially aimed at scientists from Latin America and iberoAmerica whose central research topic is plastic materials, eventually it could attract scientists from around the world

Font styles to use
Serif

Colors
59FF00
82FF00
B8FF75
E3FFCB
F4FFEA

Requirements
Must have
• From the beginning in the announcement of the appearance of this new journal, it must capture the attention of the public, the project will be presented at the main annual meeting of the Collective of Verdant Fibers
Nice to have
• in the ppt file I send there is alogo involving two persons exchanging ideas. a variant of this logo will nice to have in the cover page of the journal
Should not have
• the name of current international journals.

```html
<!DOCTYPE html>
<html lang="es">
<head>
<meta charset="utf-8">
<title>Verdant Fiber Collective Review — Cover</title>
<link href="https://fonts.googleapis.com/css2?family=Poppins:wght@400;500;600;700;800&display=swap" rel="stylesheet">
<style>
  :root {
    --stage: #6e6e6e;
    --page-top: #c3e6e8;
    --page-mid: #a6e2e8;
    --page-bottom: #79dcea;
    --green: #10794f;
    --orange: #ee5a2c;
    --ink: #1f2a2a;
    --ink-soft: #33403f;
    --navy: #1a3f8f;
    --mint: #5fb89b;
  }
  * { margin: 0; padding: 0; box-sizing: border-box; }
  html, body { width: 1200px; height: 867px; overflow: hidden; }
  body {
    background: var(--stage);
    font-family: "Poppins", sans-serif;
    color: var(--ink);
    position: relative;
  }
  .spread {
    position: absolute;
    left: 160px; top: 130px;
    width: 880px; height: 606px;
    display: flex;
    box-shadow: 0 18px 40px rgba(0,0,0,.35);
  }
  .page {
    position: relative;
    width: 440px; height: 606px;
    background: linear-gradient(180deg, var(--page-top) 0%, var(--page-mid) 55%, var(--page-bottom) 100%);
    overflow: hidden;
  }
  .back-cover { border-right: 1px solid rgba(0,0,0,.08); }

  /* Back cover */
  .masthead-small {
    position: absolute; left: 58px; top: 34px;
    font-weight: 800; line-height: .98; font-size: 27px; letter-spacing: -.3px;
  }
  .masthead-small .green { color: var(--green); display: block; }
  .masthead-small .orange { color: var(--orange); display: block; }
  .masthead-small .sub {
    display: block; font-size: 9px; font-weight: 700; letter-spacing: 4.5px;
    color: var(--green); margin-top: 4px;
  }
  .editor-block { position: absolute; left: 52px; top: 132px; }
  .editor-label { font-size: 10px; letter-spacing: 2px; font-weight: 500; color: var(--ink-soft); }
  .editor-name { font-size: 15px; font-weight: 700; color: var(--ink); }

  .board { position: absolute; left: 36px; top: 196px; width: 190px; }
  .committee { position: absolute; left: 230px; top: 232px; width: 200px; }
  .section-title { font-size: 12px; font-weight: 700; margin-bottom: 6px; }
  .board .section-title { color: var(--green); }
  .committee .section-title { color: var(--orange); }
  .member-list { list-style: none; font-size: 7.2px; line-height: 1.35; color: var(--ink-soft); }
  .board .member-list li { margin-bottom: 6px; }
  .committee .member-list li { margin-bottom: 4px; }

  .partner-logos {
    position: absolute; left: 36px; top: 490px;
    display: flex; align-items: center; gap: 18px;
  }
  .partner-name { font-size: 24px; font-weight: 700; color: var(--navy); }
  .partner-secondary { display: flex; align-items: center; gap: 5px; font-size: 11px; font-weight: 600; color: var(--navy); }
  .legal-notice {
    position: absolute; left: 212px; top: 488px; width: 196px;
    font-size: 5.6px; line-height: 1.45; color: var(--ink-soft);
  }

  /* Front cover */
  .masthead-large {
    position: absolute; left: 32px; top: 44px;
    font-weight: 800; line-height: .92; font-size: 54px; letter-spacing: -1px;
  }
  .masthead-large .green { color: var(--green); display: block; }
  .masthead-large .orange { color: var(--orange); display: block; }
  .masthead-large .sub {
    display: block; font-size: 13px; font-weight: 700; letter-spacing: 7px;
    color: var(--ink); margin-top: 8px;
  }
  .journal-mark {
    position: absolute; right: 26px; top: 120px;
    display: flex; flex-direction: column; align-items: center; gap: 4px;
    font-size: 9px; font-weight: 700; color: var(--ink);
  }
  .journal-mark .dot { width: 26px; height: 26px; border-radius: 50%; background: var(--mint); }
  .motto {
    position: absolute; left: 34px; top: 372px; width: 200px;
    font-size: 21px; line-height: 1.18; font-weight: 400; color: var(--ink);
  }
  .cover-art {
    position: absolute; right: 0; top: 290px; width: 210px; height: 300px;
  }
</style>
</head>
<body>
  <main class="spread">
    <section class="page back-cover">
      <h2 class="masthead-small">
        <span class="green">THE VERDANT</span>
        <span class="orange">FIBER COLLECTIVE</span>
        <span class="sub">REVIEW(VFCR)</span>
      </h2>

      <div class="editor-block">
        <p class="editor-label">EDITOR IN CHIEF</p>
        <p class="editor-name">Dr. Lucio Ferran-Abad</p>
      </div>

      <div class="board">
        <h3 class="section-title">EDITORIAL BOARD</h3>
        <ul class="member-list">
          <li>Dr. Tobías Lerma Quintal<br>TLOK)</li>
          <li>Dr. Iván Robledo<br>(IMRV)</li>
          <li>Dr. Marco Ceballos<br>(UA del Norte)</li>
          <li>Dr. Elías Parra<br>(ITCosta)</li>
          <li>Dr. Saúl Medina Oria.</li>
          <li>Dr. Andrés Villa Toral<br>(Universidad del Bajío Verde)</li>
          <li>Dr. Saúl Medina Oria<br>(universidad de Altamira)</li>
          <li>J. Noemí Ruiz CAMPA<br>(UNIVERSIDAD LACUSTRE)</li>
        </ul>
      </div>

      <div class="committee">
        <h3 class="section-title">EDITORIAL COMMITEE</h3>
        <ul class="member-list">
          <li>Dr. Tobías Lerma Quintal(TLOK)</li>
          <li>Dr. Iván Robledo(IMRV)</li>
          <li>Dr. Marco Ceballos (UA del Norte)</li>
          <li>Dr. Elías Parra Montiel</li>
          <li>Dr. Saúl Medina Oria</li>
          <li>Dr. Andrés Villa Toral<br>(Universidad del Bajío Verde)</li>
          <li>Dr. Saúl Medina Oria<br>(universidad de Altamira)</li>
          <li>J. Noemí Ruiz CAMPA<br>(UNIVERSIDAD LACUSTRE)</li>
          <li>Dr. Hugo Salas Ibarra</li>
          <li>Dr. Pablo Ureña</li>
          <li>Dr. Nadia Lozano Reyes</li>
        </ul>
      </div>

      <div class="partner-logos">
        <span class="partner-name">TLOK</span>
        <span class="partner-secondary">
          <svg width="14" height="14" aria-hidden="true"><circle cx="7" cy="7" r="7" fill="var(--navy)"/></svg>
          Ravendix
        </span>
      </div>

      <p class="legal-notice">RVFC, vol. 5, núm. 12, septiembre 2023–febrero 2024, es una revista académica digital de acceso libre y publicación cuatrimestral editada por TLOK con apoyo de Ravendix. Calle Ficticia 100, Col. Centro, C.P. 00000. Tel. +00 (000) 000 0000. Contacto: editorial@vfcr.example. Última modificación: 21 de septiembre de 2023.</p>
    </section>

    <section class="page front-cover">
      <h1 class="masthead-large">
        <span class="green">THE</span>
        <span class="green">VERDANT</span>
        <span class="orange">FIBER</span>
        <span class="green">COLLECTIVE</span>
        <span class="sub">REVIEW(VFCR)</span>
      </h1>

      <div class="journal-mark">
        <span class="dot"></span>
        <span>JOURNAL CVF</span>
      </div>

      <p class="motto">The RVFC lifts Fiber Craft and inspires a Bright Tomorrow.</p>

      <svg class="cover-art" viewBox="0 0 210 300" role="img" aria-label="Illustration of a ball-and-stick molecular model in orange, teal and white">
        <defs>
          <radialGradient id="artTone" cx="55%" cy="45%" r="65%">
            <stop offset="0%" stop-color="#f07a45" stop-opacity=".75"/>
            <stop offset="55%" stop-color="#2fae8f" stop-opacity=".45"/>
            <stop offset="100%" stop-color="#7fdcea" stop-opacity="0"/>
          </radialGradient>
        </defs>
        <rect width="210" height="300" fill="url(#artTone)"/>
      </svg>
    </section>
  </main>
</body>
</html>
```